Business Card Design

We are an IT staffing and consulting company providing IT solutions and resources to our clients.

Industry/Entity Type

Business

Contact Information for Business Card

Ramesh Tulavarthi
Vice President

BrightNode Inc
48215 Harrowmere Court Square, suite 700
Ashburn, VA 20147
Direct: 571-555-0193
Mobile: 571-555-0147
Email: Ramesh@brightnodeinc.com
Fax: 703-555-0162
www.brightnodeinc.com

```html
<!DOCTYPE html>
<html lang="en">
<head>
<meta charset="utf-8">
<title>BrightNode Inc — Business Card</title>
<link rel="stylesheet" href="https://fonts.googleapis.com/css2?family=Open+Sans:wght@400;600;700&display=swap">
<style>
  :root {
    --backdrop: #2b2927;
    --card-black: #0b0b0c;
    --card-edge: #2a3032;
    --accent-red: #d4161f;
    --text-white: #f2f2f2;
    --text-soft: #d9d9d9;
  }
  * { box-sizing: border-box; margin: 0; padding: 0; }
  html, body {
    width: 1200px; height: 844px; overflow: hidden;
    background: var(--backdrop);
    font-family: "Open Sans", Arial, sans-serif;
  }
  .stage { position: relative; width: 1200px; height: 844px; }
  .card {
    position: absolute;
    width: 520px; height: 298px;
    top: 273px;
    border-radius: 3px;
    overflow: hidden;
    background: linear-gradient(100deg, var(--card-black) 0%, #111214 55%, var(--card-edge) 100%);
    color: var(--text-white);
  }
  .card--front { left: 50px; }
  .card--back { left: 630px; }

  .brand {
    position: absolute;
    display: flex; align-items: center; gap: 10px;
    font-weight: 600; color: var(--text-white);
    letter-spacing: 0.5px; white-space: nowrap;
  }
  .brand__mark { width: 14px; height: 14px; background: var(--accent-red); flex: none; }
  .card--front .brand { top: 56px; left: 262px; font-size: 24px; }
  .card--back .brand { top: 124px; left: 130px; font-size: 32px; }
  .card--back .brand__mark { width: 18px; height: 18px; }

  .person { position: absolute; top: 92px; left: 40px; }
  .person__name {
    color: var(--accent-red); font-weight: 600; font-size: 19px; line-height: 1.1;
  }
  .person__title { color: var(--text-soft); font-size: 12.5px; margin-top: 3px; }

  .address {
    position: absolute; top: 144px; left: 40px;
    font-size: 12.5px; line-height: 16px; color: var(--text-soft);
  }
  .contacts {
    position: absolute; top: 200px; left: 40px;
    list-style: none; font-size: 13px; color: var(--text-white);
  }
  .contacts li { display: flex; align-items: center; gap: 10px; height: 17.5px; }
  .contacts__icon {
    width: 14px; height: 14px; border-radius: 3px;
    background: var(--accent-red);
    display: flex; align-items: center; justify-content: center;
    flex: none;
  }
  .contacts__icon svg { width: 10px; height: 10px; }
</style>
</head>
<body>
<main class="stage">
  <section class="card card--front" aria-label="Business card front">
    <div class="person">
      <p class="person__name">Ramesh Tulavarthi</p>
      <p class="person__title">Vice President</p>
    </div>

    <div class="brand"><span class="brand__mark"></span><span>BrightNode Inc</span></div>

    <p class="address">48215 Harrowmere Court Square, suite 700<br>Ashburn, VA 20147</p>

    <ul class="contacts">
      <li>
        <span class="contacts__icon">
          <svg viewBox="0 0 10 10"><path d="M1 3.5 C1 2 3 1.5 5 1.5 S9 2 9 3.5 L7 4 L6.6 3 H3.4 L3 4 Z M2.5 5 H7.5 L8.5 8.5 H1.5 Z" fill="#fff"/></svg>
        </span>
        571-555-0193
      </li>
      <li>
        <span class="contacts__icon">
          <svg viewBox="0 0 10 10"><rect x="2.8" y="0.8" width="4.4" height="8.4" rx="0.8" fill="#fff"/><rect x="3.6" y="2" width="2.8" height="5" fill="#d4161f"/></svg>
        </span>
        571-555-0147
      </li>
      <li>
        <span class="contacts__icon">
          <svg viewBox="0 0 10 10"><rect x="1" y="2.5" width="8" height="5.5" fill="#fff"/><path d="M1 2.5 L5 6 L9 2.5" stroke="#d4161f" stroke-width="0.9" fill="none"/></svg>
        </span>
        Ramesh@brightnodeinc.com
      </li>
      <li>
        <span class="contacts__icon">
          <svg viewBox="0 0 10 10"><rect x="1.5" y="3.5" width="7" height="5" fill="#fff"/><rect x="3" y="1" width="4" height="3" fill="#fff"/><rect x="3" y="5" width="4" height="1" fill="#d4161f"/></svg>
        </span>
        703-555-0162
      </li>
      <li>
        <span class="contacts__icon">
          <svg viewBox="0 0 10 10"><g fill="none" stroke="#fff" stroke-width="1.4"><rect x="1" y="5" width="4.5" height="2.6" rx="1.3" transform="rotate(-45 3.2 6.3)"/><rect x="4.5" y="2.4" width="4.5" height="2.6" rx="1.3" transform="rotate(-45 6.8 3.7)"/></g></svg>
        </span>
        www.brightnodeinc.com
      </li>
    </ul>
  </section>

  <section class="card card--back" aria-label="Business card back">
    <div class="brand"><span class="brand__mark"></span><span>BrightNode Inc</span></div>
  </section>
</main>
</body>
</html>
```